Business card for international trading company
Dear Project Holder...thanks for giving me 5 star, I saw your project really in the end time, if u want any changes in this design, just let me know and I do it for u...
regards...
For #183,
Please minimize the size of the logo so you can include the arabic name. Please also use the following fonts:
http://www.pixorambe.net/photos/morlin_studio/5821904637/
Use P for the phone and F for fax. You can also mention the email and website without words like email and website before.
Please use fonts as the following:
Try also to use P for the phone and F for fax. You can also mention the email and website without words like email and website before.
I AM STILL WAITING FOR CREATIVE AND EXCLUSIVE IDEAS!
#138 might be an example of a special idea for this project, but we are expecting MOOOORE creative and wonderful designs!
LOOK AT THESE DESIGNS:
http://www.quillnovaprints.com/inspiration/minimal-business-cards/
Please let us see your creativity!
I am looking for more creative ideas which are unique and deigned especially for this project.
One thing to point out, you can exclude the fax to make more space. You can also exclude the website from the front and just include it on the back of the card.
IMPORTANT: If you think it looks good, you can make use of our slogan "Envisioning Tomorrow" to be included with the logo on the back of the card.
I am still waiting for MORE creative ideas. I uploaded the figure used in our logo as 2D. Please find it as an attachment. It might be useful.
Please refer to the following link to find very creative ideas:

```html
<!DOCTYPE html>
<html lang="en">
<head>
<meta charset="utf-8">
<title>Saltwind Business Card</title>
<link rel="stylesheet" href="https://fonts.googleapis.com/css2?family=Source+Sans+3:wght@400;600;700&display=swap">
<style>
  :root {
    --page-bg: #e9e7e3;
    --card-bg: #ffffff;
    --band-navy: #2f2e8f;
    --band-light: #4aa3df;
    --brand: #2f3a96;
    --brand-dot: #6a4fb3;
    --ink: #4a4a4a;
    --icon: #2f3a96;
    --rule: #c9c9cf;
  }
  * { margin: 0; padding: 0; box-sizing: border-box; }
  html, body {
    width: 1200px; height: 780px; overflow: hidden;
    background: var(--page-bg);
    font-family: "Source Sans 3", "Myriad Pro", Arial, sans-serif;
  }
  .card {
    position: absolute; left: 80px; top: 93px;
    width: 1040px; height: 594px;
    background: var(--card-bg);
    border-radius: 30px;
    overflow: hidden;
    box-shadow: 0 10px 28px rgba(0,0,0,0.18);
  }
  .card-band { position: absolute; left: 0; top: 0; width: 1040px; height: 240px; }
  .holder {
    position: absolute; right: 44px; top: 42px;
    text-align: right; color: #fff;
  }
  .holder-name { font-size: 30px; font-weight: 700; line-height: 1.1; }
  .holder-title { font-size: 22px; font-weight: 400; line-height: 1.3; }
  .brand {
    position: absolute; left: 40px; top: 280px; width: 330px;
    display: flex; flex-direction: column; align-items: center;
  }
  .brand-dot {
    width: 120px; height: 120px; border-radius: 50%;
    background: var(--brand-dot);
  }
  .brand-name {
    margin-top: 34px;
    font-size: 62px; font-weight: 700; letter-spacing: 1px;
    color: var(--brand); line-height: 1;
  }
  .divider {
    position: absolute; left: 420px; top: 250px;
    width: 2px; height: 300px; background: var(--rule);
  }
  .contact {
    position: absolute; left: 446px; top: 262px;
    list-style: none; color: var(--ink);
    font-size: 21px; line-height: 33px;
  }
  .contact li { display: flex; align-items: center; height: 33px; }
  .contact .address { padding-left: 32px; }
  .contact svg { width: 20px; height: 20px; margin-right: 12px; flex: none; fill: var(--icon); }
</style>
</head>
<body>
<main class="card">
  <svg class="card-band" viewBox="0 0 1040 240" aria-hidden="true">
    <path d="M0 0 H1040 V168 C820 118 520 130 300 160 C180 176 80 192 0 198 Z" fill="var(--band-navy)"/>
    <path d="M0 198 C80 192 180 176 300 160 C520 130 820 118 1040 168 V184 C820 140 520 148 300 176 C180 190 80 204 0 210 Z" fill="var(--band-light)"/>
  </svg>

  <header class="holder">
    <p class="holder-name">Khalid R. Al-Mansour</p>
    <p class="holder-title">Managing Partner</p>
  </header>

  <div class="brand">
    <div class="brand-dot"></div>
    <p class="brand-name">SALTWIND</p>
  </div>

  <div class="divider"></div>

  <ul class="contact">
    <li class="address">P.O. Box 5318 Dammam</li>
    <li class="address">Saudi Arabia</li>
    <li><svg viewBox="0 0 24 24"><path d="M6.6 10.8a15 15 0 0 0 6.6 6.6l2.2-2.2a1 1 0 0 1 1-.25 11.4 11.4 0 0 0 3.6.57 1 1 0 0 1 1 1V20a1 1 0 0 1-1 1A17 17 0 0 1 3 4a1 1 0 0 1 1-1h3.5a1 1 0 0 1 1 1c0 1.25.2 2.45.57 3.57a1 1 0 0 1-.25 1z"/></svg>+966 3 827 5064 Ext. 214</li>
    <li><svg viewBox="0 0 24 24"><path d="M7 1h10a2 2 0 0 1 2 2v18a2 2 0 0 1-2 2H7a2 2 0 0 1-2-2V3a2 2 0 0 1 2-2zm0 3v14h10V4zm5 15.5a1.2 1.2 0 1 0 0 2.4 1.2 1.2 0 0 0 0-2.4z"/></svg>+966 551 308 926</li>
    <li><svg viewBox="0 0 24 24"><path d="M6 2h9l3 3v5H6zm-2 9h16a2 2 0 0 1 2 2v7a2 2 0 0 1-2 2H4a2 2 0 0 1-2-2v-7a2 2 0 0 1 2-2zm2 3v2h3v-2zm5 0v2h3v-2zm5 0v2h3v-2z"/></svg>+966 3 827 5190</li>
    <li><svg viewBox="0 0 24 24"><path d="M12 2a10 10 0 1 0 5 18.7l-1-1.7A8 8 0 1 1 20 12v1a2 2 0 0 1-4 0V7h-2v1a5 5 0 1 0 .6 6.9A4 4 0 0 0 22 13v-1A10 10 0 0 0 12 2zm0 13a3 3 0 1 1 0-6 3 3 0 0 1 0 6z"/></svg>khalid.mansour@saltwind.com</li>
    <li><svg viewBox="0 0 24 24"><path d="M12 2a10 10 0 1 0 0 20 10 10 0 0 0 0-20zm6.9 6h-3a15 15 0 0 0-1.3-3.9A8 8 0 0 1 18.9 8zM12 4c.8 1.2 1.5 2.5 1.9 4h-3.8c.4-1.5 1.1-2.8 1.9-4zM4.3 14a8 8 0 0 1 0-4h3.4a16 16 0 0 0 0 4zm.8 2h3a15 15 0 0 0 1.3 3.9A8 8 0 0 1 5.1 16zm3-8h-3a8 8 0 0 1 4.3-3.9A15 15 0 0 0 8.1 8zM12 20c-.8-1.2-1.5-2.5-1.9-4h3.8c-.4 1.5-1.1 2.8-1.9 4zm2.3-6H9.7a14 14 0 0 1 0-4h4.6a14 14 0 0 1 0 4zm.3 5.9a15 15 0 0 0 1.3-3.9h3a8 8 0 0 1-4.3 3.9zm1.7-5.9a16 16 0 0 0 0-4h3.4a8 8 0 0 1 0 4z"/></svg>www.saltwind.com</li>
  </ul>
</main>
</body>
</html>
```